Bright Oak Fitness Facility Business Cards

Business Card Design that incorporates the logo and tagline

Target Market(s)

Fitness, People Who Exercise

Contact Information for Business Card

2817 Mossgrove Bend Road
Tavares, Florida 32190
Phone: 352-555-Jump (5867)
www.brightoakfitness.example
info@brightoakfitness.example

Requirements
Must have
• Logo, Address, Website, email and tagline "More Than A Gym". Colors should be red/black/grey/white

```html
<!DOCTYPE html>
<html lang="en">
<head>
<meta charset="utf-8">
<title>Bright Oak Fitness – Business Cards</title>
<link rel="stylesheet" href="https://fonts.googleapis.com/css2?family=Arimo:wght@400;700&display=swap">
<style>
  :root {
    --bg: #dcdcdc;
    --ink: #121212;
    --paper: #e4e4e4;
    --red: #d42027;
    --light: #f0f0f0;
  }
  * { box-sizing: border-box; margin: 0; padding: 0; }
  html, body { width: 1200px; height: 1200px; overflow: hidden; }
  body {
    background: var(--bg);
    font-family: "Arimo", Arial, sans-serif;
    position: relative;
  }
  .card {
    position: absolute;
    left: 227px;
    width: 746px;
    height: 425px;
    overflow: hidden;
  }
  .card--front { top: 135px; background: var(--ink); }
  .card--back { top: 639px; background: var(--ink); }

  .front__brand-panel {
    position: absolute;
    left: 0; top: 0;
    width: 393px; height: 100%;
    background: var(--paper);
    display: flex;
    align-items: center;
    justify-content: center;
  }
  .front__divider {
    position: absolute;
    left: 393px; top: 0;
    width: 6px; height: 100%;
    background: var(--red);
  }
  .brand {
    display: flex;
    align-items: center;
    gap: 10px;
    font-weight: 700;
    color: var(--red);
    white-space: nowrap;
  }
  .brand__mark {
    width: 18px; height: 18px;
    background: var(--red);
    flex: none;
  }
  .brand__name { font-size: 34px; letter-spacing: -0.5px; }
  .card--back .brand { position: absolute; left: 0; right: 0; top: 180px; justify-content: center; }
  .card--back .brand__name { font-size: 46px; }
  .card--back .brand__mark { width: 24px; height: 24px; }

  .contact {
    position: absolute;
    left: 447px;
    color: var(--light);
  }
  .contact__name {
    top: 107px;
    font-size: 24px;
    font-weight: 400;
    color: var(--red);
    letter-spacing: 0.2px;
  }
  .contact__role { top: 138px; font-size: 17px; }
  .contact__address { top: 180px; font-size: 17px; line-height: 24px; }
  .contact__lines {
    top: 272px;
    list-style: none;
    font-size: 17px;
    line-height: 23.5px;
  }
  .contact__lines li { display: flex; align-items: center; gap: 10px; }
  .contact__lines svg { width: 15px; height: 15px; flex: none; }

  .tagline {
    position: absolute;
    left: 0; right: 0; top: 374px;
    text-align: center;
    color: var(--red);
    font-size: 17px;
  }
</style>
</head>
<body>

<section class="card card--front" aria-label="Business card front">
  <div class="front__brand-panel">
    <div class="brand"><span class="brand__mark"></span><span class="brand__name">Bright Oak Fitness</span></div>
  </div>
  <div class="front__divider"></div>

  <h1 class="contact contact__name">DANIEL HARWICK</h1>
  <p class="contact contact__role">Managing Director</p>
  <p class="contact contact__address">2817 Mossgrove Bend Road<br>Tavares, Florida 32190</p>
  <ul class="contact contact__lines">
    <li>
      <svg viewBox="0 0 16 16" aria-hidden="true"><path fill="#d42027" d="M1 6c0-2 3-3 7-3s7 1 7 3v1h-3V5.5H4V7H1zM4 8l2-3h4l2 3v5H4z"/><circle cx="8" cy="10" r="1.6" fill="#121212"/></svg>
      <span>352-555-Jump (5867)</span>
    </li>
    <li>
      <svg viewBox="0 0 16 16" aria-hidden="true"><rect x="1.5" y="3.5" width="13" height="9" fill="none" stroke="#d42027" stroke-width="1.4"/><path d="M1.5 3.5 8 9l6.5-5.5" fill="none" stroke="#d42027" stroke-width="1.4"/></svg>
      <span>info@brightoakfitness.example</span>
    </li>
    <li>
      <svg viewBox="0 0 16 16" aria-hidden="true"><circle cx="8" cy="8" r="7" fill="#d42027"/><path d="M3 5c2 0 3 1 3 3s2 2 1 4M9 2c0 2 2 2 3 4" fill="none" stroke="#121212" stroke-width="1.3"/></svg>
      <span>www.brightoakfitness.example</span>
    </li>
  </ul>
</section>

<section class="card card--back" aria-label="Business card back">
  <div class="brand"><span class="brand__mark"></span><span class="brand__name">Bright Oak Fitness</span></div>
  <p class="tagline">MORE THAN A GYM</p>
</section>

</body>
</html>
```